We need a website that entices australia's workers to sign up to help protect their industry and their jobs. The key message is "Building a Stronger Australia" and that headline / tagline should feature prominently on the site.

In terms of style I lack the current 'scrolling' style (see example http://www.pebblelane.ca )

The site must dynamically for mobile platforms. It must also use Joomla or Wordpress as CMS so is client editable.

The attached logo is the basis for the design and the name of the organisation is the Enduring Progress Council. Please make an allowance for an iframe embed (min height 650px) see attached sample.

It should also have a subscriber sign up for that connects with Mailing Beacon

Attached text for front page is DRAFT ONLY

Target Market(s)

Working class australians, (eg miners, farmers, factory workers, etc)

Industry/Entity Type

Industry

Coding

Coded - Design and coding required

Number of Pages Required

4 page

Requirements
Must have
• An editable CMS
• Subscription form connecting with Mailing Beacon (see https://kelvoram.postriver.com/help/topic.aspx?t=13)
• Must resize for mobile
• Must allow for an iframe
Nice to have
• It must have a friendly feel but strong, not 'girly' though should not alienate women
Should not have
• Images that are not australian
• Images that do not have the appropriate rights to use

```html
<!DOCTYPE html>
<html lang="en">
<head>
<meta charset="utf-8">
<title>Enduring Progress Council — Building a Stronger Australia</title>
<link href="https://fonts.googleapis.com/css2?family=Raleway:wght@500;600;700&family=Open+Sans:wght@400;600;700&display=swap" rel="stylesheet">
<style>
:root{
  --orange:#e5582b;
  --amber:#f39b26;
  --red:#df3f1e;
  --brown:#7a2c12;
  --ink:#444;
  --ink-dark:#333;
  --grey-bg:#e8e8e8;
  --circle-grey:#e4e4e4;
  --footer:#3e3b3a;
  --footer-bottom:#2f2c2b;
  --white:#fff;
  --head:'Raleway',sans-serif;
  --body:'Open Sans',sans-serif;
}
*{box-sizing:border-box;margin:0;padding:0}
html,body{width:1200px;height:3249px;overflow:hidden}
body{font-family:var(--body);color:var(--ink);background:var(--white);position:relative}
section,header,footer{position:relative;width:1200px;overflow:hidden}
.abs{position:absolute}

/* header */
.site-header{height:120px;background:var(--white)}
.brand{left:83px;top:30px;display:flex;align-items:center;gap:12px}
.brand-dot{width:56px;height:56px;border-radius:50%;background:var(--orange)}
.brand-name{font-family:var(--head);font-weight:700;color:var(--ink-dark);line-height:1}
.brand-name b{display:block;font-size:36px}
.brand-name small{display:block;font-size:11px;margin-top:2px}
.main-nav{right:82px;top:56px;display:flex;gap:30px;font-family:var(--head);font-weight:700;font-size:14px;color:var(--ink-dark)}
.main-nav .active{border-bottom:3px solid var(--orange);padding-bottom:6px}

/* hero */
.hero{height:638px}
.hero-photo{inset:0;background:linear-gradient(180deg,#b5694a 0%,#c9794f 35%,#c66c3f 70%,#b9643e 100%)}
.hero-box{left:553px;top:216px;width:565px;height:306px;background:rgba(45,28,20,.78);border-bottom:5px solid var(--orange);padding:40px 52px}
.hero-box h1{font-family:var(--head);font-weight:700;font-size:62px;line-height:68px;color:var(--white)}

/* intro band */
.intro{height:481px;background:linear-gradient(180deg,#e35c30,#d84c22);text-align:center;color:var(--white)}
.intro h2{font-family:var(--head);font-weight:700;font-size:47px;line-height:61px;width:760px;margin:52px auto 0}
.intro p{font-size:15px;line-height:23px;width:820px;margin:42px auto 0}
.btn-dark{display:inline-block;margin-top:37px;background:#3b3533;color:var(--white);font-size:16px;width:139px;height:38px;line-height:38px;border-radius:3px}

/* divest */
.divest{height:489px}
.icon-circle{width:196px;height:196px;border-radius:50%;display:flex;align-items:center;justify-content:center}
.divest .icon-circle{left:113px;top:68px;background:var(--circle-grey)}
.divest h2{left:375px;top:76px;width:700px;font-family:var(--head);font-weight:700;font-size:44px;line-height:56px;color:var(--ink)}
.divest .lead{left:375px;top:272px;font-weight:700;font-size:14px;color:var(--ink-dark)}
.reasons{left:378px;top:298px;list-style:none;font-size:14.5px;line-height:25.5px;color:var(--ink)}
.reasons li{display:flex;align-items:center;gap:14px}
.reasons li::before{content:"";width:14px;height:14px;border-radius:50%;background:var(--red);flex:none}

/* email band */
.email-band{height:481px;background:linear-gradient(90deg,#f5a329 0%,#f29a25 65%,#e8932d 100%)}
.email-photo{right:0;top:0;width:270px;height:481px;background:linear-gradient(180deg,rgba(255,210,140,.35),rgba(200,120,40,.35))}
.email-band .icon-circle{left:107px;top:122px;background:var(--white)}
.email-band h2{left:375px;top:40px;font-family:var(--head);font-weight:700;font-size:42px;color:var(--white)}
.email-band .sub{left:376px;top:117px;width:720px;font-size:14px;line-height:28px;font-weight:600;color:var(--white)}
.email-band .prompt{left:376px;top:192px;font-size:14px;font-weight:600;color:var(--white)}
.field{height:43px;background:var(--white);border:1px solid #ddd;font-size:14px;color:#aaa;padding:0 12px;display:flex;align-items:center;justify-content:space-between}
.btn{height:42px;width:141px;color:var(--white);font-weight:700;font-size:15px;display:flex;align-items:center;justify-content:center}
.btn-submit{background:var(--red)}
.btn-cancel{background:var(--brown)}

/* get started */
.get-started{height:256px;text-align:center}
.get-started h2{font-family:var(--head);font-weight:700;font-size:44px;color:var(--ink);margin-top:48px}
.get-started p{color:var(--red);font-size:16px;line-height:24px;width:860px;margin:26px auto 0}

/* testimonials */
.testimonials{height:321px;background:var(--grey-bg)}
.testimonials h2{left:0;width:1200px;top:36px;text-align:center;font-family:var(--head);font-weight:700;font-size:44px;color:var(--ink)}
.avatar{width:122px;height:122px;border-radius:50%;background:linear-gradient(180deg,#c9d3da,#9a7c5e)}
.quote{width:290px;font-size:13.5px;line-height:22px;color:var(--ink);border-left:1px solid #ccc;padding-left:22px}

/* footer */
.site-footer{height:464px;background:var(--footer);color:var(--white)}
.site-footer .brand{top:46px}
.site-footer .brand-name{color:var(--white)}
.contact{left:83px;top:115px;font-size:13px;line-height:22px}
.follow{left:83px;top:250px;font-size:17px}
.socials{left:83px;top:285px;display:flex;gap:8px}
.socials span{width:26px;height:26px;border-radius:50%}
.locate{left:597px;top:36px;font-family:var(--head);font-size:29px;font-weight:500}
.map{left:600px;top:84px;width:518px;height:190px;background:linear-gradient(135deg,#e8e4dc,#d9d3c4)}
.news-label{left:597px;top:290px;font-family:var(--head);font-size:21px;font-weight:500}
.news-row{left:600px;top:321px;display:flex;gap:6px}
.news-row .field{height:30px;width:176px;color:var(--ink);font-size:14px}
.news-row .btn{height:30px;width:131px;background:var(--red);font-size:14px;font-weight:600}
.bottom-bar{left:0;bottom:0;width:1200px;height:78px;background:var(--footer-bottom);font-size:12px;color:#bbb;display:flex;justify-content:space-between;align-items:center;padding:0 83px}
</style>
</head>
<body>

<header class="site-header">
  <div class="brand abs"><span class="brand-dot"></span><span class="brand-name"><b>EPC</b><small>Enduring Progress Council</small></span></div>
  <nav class="main-nav abs"><span class="active">TAKE ACTION</span><span>ABOUT</span><span>FACTS</span><span>NEWS</span><span>CONTACT</span></nav>
</header>

<section class="hero">
  <div class="hero-photo abs" role="img" aria-label="Photo of a mine worker in a hard hat standing on red earth at an open-cut mine site"></div>
  <div class="hero-box abs"><h1>BUILDING A STRONGER AUSTRALIA</h1></div>
</section>

<section class="intro">
  <h2>Lorem Ipsum is simply dummy text of the printing and typesetting industry.</h2>
  <p>Lorem Ipsum is simply dummy text of the printing and typesetting industry. Lorem Ipsum has been the industry's standard dummy text ever since the 1500s, when an unknown printer took a galley of type and scrambled it to make a type specimen book. It has survived not only five centuries, but also the leap into electronic typesetting, remaining essentially unchanged.</p>
  <span class="btn-dark">Read More</span>
</section>

<section class="divest">
  <div class="icon-circle abs">
    <svg width="96" height="84" viewBox="0 0 96 84"><g fill="#3a3a3a"><path d="M8 30h18l44-24v68L26 50H8z"/><path d="M28 52h14l6 26H36z"/><rect x="74" y="30" width="14" height="20" rx="4"/></g></svg>
  </div>
  <h2 class="abs">Tell your Bank and Superfund you do NOT want them to divest out of Australian Industry.</h2>
  <div class="lead abs">This Could:</div>
  <ul class="reasons abs">
    <li>Cost you your job as less investment means less jobs</li>
    <li>Give you less to retire on as your superannuation fund gets strong returns from investment</li>
    <li>Reduce your hard earned savings</li>
    <li>Impact communities that rely on industry</li>
    <li>Not help the environment at all</li>
  </ul>
</section>

<section class="email-band">
  <div class="email-photo abs" role="img" aria-label="Faint photo of a worker in a hard hat"></div>
  <div class="icon-circle abs">
    <svg width="100" height="90" viewBox="0 0 100 90"><g fill="var(--amber)"><path d="M50 2 96 24H4z"/><rect x="8" y="28" width="84" height="6"/><rect x="14" y="38" width="11" height="36"/><rect x="33" y="38" width="11" height="36"/><rect x="56" y="38" width="11" height="36"/><rect x="75" y="38" width="11" height="36"/><rect x="6" y="78" width="88" height="8"/></g></svg>
  </div>
  <h2 class="abs">Email your Bank - It's Easy</h2>
  <p class="sub abs">Take a few moments to contact your bank and let them know you do not want them to divest from Australian industry. Here's your opportunity to be heard. Your voice will make a difference.</p>
  <p class="prompt abs">To get started please fill in your name and email address</p>
  <div class="field abs" style="left:377px;top:243px;width:235px">First Name</div>
  <div class="field abs" style="left:630px;top:243px;width:235px">Family Name</div>
  <div class="field abs" style="left:883px;top:243px;width:235px">Email</div>
  <div class="field abs" style="left:377px;top:309px;width:371px">Select Bank <span style="color:#555">&#8964;</span></div>
  <div class="field abs" style="left:767px;top:309px;width:351px">Superfund <span style="color:#555">&#8964;</span></div>
  <div class="btn btn-submit abs" style="left:377px;top:374px">SUBMIT</div>
  <div class="btn btn-cancel abs" style="left:529px;top:374px">CANCEL</div>
</section>

<section class="get-started">
  <h2>It's easy to get started</h2>
  <p>We have developed an advocacy centre — a place where you can send a letter or email to your bank, super fund, MP or your newspaper, share information online with your friends via social media.</p>
</section>

<section class="testimonials">
  <svg class="abs" style="left:400px;top:48px" width="24" height="40" viewBox="0 0 24 40"><path d="M20 2 4 20l16 18" fill="none" stroke="#999" stroke-width="3"/></svg>
  <h2 class="abs">Testimonials</h2>
  <svg class="abs" style="left:776px;top:48px" width="24" height="40" viewBox="0 0 24 40"><path d="M4 2l16 18L4 38" fill="none" stroke="#999" stroke-width="3"/></svg>
  <div class="avatar abs" style="left:112px;top:145px" role="img" aria-label="Portrait of a worker in a hard hat"></div>
  <p class="quote abs" style="left:275px;top:162px">Lorem Ipsum is simply dummy text of the printing and typesetting industry. Lorem Ipsum has been the industry's standard dummy text ever since the 1500s</p>
  <div class="avatar abs" style="left:628px;top:145px" role="img" aria-label="Portrait of a worker in a hard hat"></div>
  <p class="quote abs" style="left:790px;top:162px">Lorem Ipsum is simply dummy text of the printing and typesetting industry. Lorem Ipsum has been the industry's standard dummy text ever since the 1500s</p>
</section>

<footer class="site-footer">
  <div class="brand abs"><span class="brand-dot" style="width:48px;height:48px;background:var(--white)"></span><span class="brand-name"><b style="font-size:30px">EPC</b><small>Enduring Progress Council</small></span></div>
  <div class="contact abs">001 Some Street, Melbourne, Australia, 12345<br>Email: info@sturdyground.com.au<br>Telephone: (123) 456-7890<br>Fax: (123) 456-7890<br>Mobile: (123) 456-7890</div>
  <div class="follow abs">Follow Us</div>
  <div class="socials abs"><span style="background:#2f5ea8"></span><span style="background:#2aa3d8"></span><span style="background:#d9372a"></span></div>
  <div class="locate abs">Locate Us</div>
  <div class="map abs" role="img" aria-label="Street map showing the office location in Melbourne"></div>
  <div class="news-label abs">Email News Letter</div>
  <div class="news-row abs"><div class="field">Name</div><div class="field" style="width:206px">Email</div><div class="btn">SUBSCRIBE</div></div>
  <div class="bottom-bar abs"><span>© 2014 Enduring Progress Council. All rights reserved</span><span>Sitemap &nbsp; Privacy Policy</span></div>
</footer>

</body>
</html>
```